New letterhead and business cards for dental office

I need a new letterhead, envelopes, and business cards for our 2 dental offices. The letterhead should be able to be used at either office. A professional elegant look is desired.
Exact particulars such as the address, phone numbers etc will be provided later.
***** a reminder: we have 2 separate locations, so the letterhead needs to have 2 sets of addresses, phones numbers, etc.
Our previous letterhead had a check box to indicate which of the two offices we were corresponding from. I would like some creative ideas here.
Industry/Entity Type
Dental
Font styles to use
Look and feel
Each slider illustrates characteristics of the customer's brand and the style your logo design should communicate.

```html
<!DOCTYPE html>
<html lang="en">
<head>
<meta charset="utf-8">
<title>Ridgeway &amp; Alder — Stationery Set</title>
<link rel="stylesheet" href="https://fonts.googleapis.com/css2?family=Questrial&family=Open+Sans:wght@400;600;700&display=swap">
<style>
  :root {
    --navy: #2e3a74;
    --blue: #3c69b4;
    --paper: #ffffff;
    --backdrop: #ececec;
    --ink-soft: #5a6275;
    --tint: rgba(60,105,180,0.16);
    --tint-light: rgba(255,255,255,0.07);
    --shadow: 0 2px 6px rgba(0,0,0,0.12), 0 10px 24px rgba(0,0,0,0.08);
  }
  * { box-sizing: border-box; margin: 0; padding: 0; }
  html, body { width: 1200px; height: 870px; overflow: hidden; }
  body {
    background: var(--backdrop);
    font-family: "Open Sans", sans-serif;
    position: relative;
  }

  .brand {
    display: inline-flex;
    align-items: center;
    gap: 8px;
    font-family: "Questrial", sans-serif;
    font-weight: 400;
    color: var(--navy);
    white-space: nowrap;
  }
  .brand-dot { width: 11px; height: 11px; border-radius: 50%; background: var(--blue); flex: none; }
  .brand--light { color: #ffffff; }
  .brand--light .brand-dot { background: #ffffff; }

  .brand-graphic {
    position: absolute;
    background: linear-gradient(135deg, var(--tint), rgba(46,58,116,0.22));
    border-radius: 0 0 0 100%;
  }

  /* Business cards */
  .card {
    position: absolute;
    left: 40px;
    width: 290px;
    height: 166px;
    box-shadow: var(--shadow);
    overflow: hidden;
  }
  .card--front { top: 40px; background: var(--paper); padding: 22px; }
  .card--front .brand { font-size: 19px; }
  .card--front .brand-graphic { top: 0; right: 0; width: 70px; height: 62px; }
  .card-person { margin-top: 34px; font-size: 10px; font-weight: 700; color: var(--navy); letter-spacing: 0.06em; text-transform: uppercase; }
  .card-role { font-size: 9px; color: var(--ink-soft); margin-top: 2px; }
  .card-contact { margin-top: 10px; font-size: 9px; line-height: 1.55; color: var(--ink-soft); }
  .card-contact b { color: var(--blue); font-weight: 700; }

  .card--back {
    top: 226px;
    background: var(--navy);
    display: flex; align-items: center; justify-content: center;
  }
  .card--back .brand { font-size: 21px; }

  /* Notebook */
  .notebook {
    position: absolute;
    left: 40px; top: 420px;
    width: 290px; height: 410px;
    background: var(--navy);
    box-shadow: var(--shadow);
    padding: 44px 26px 0 46px;
    overflow: hidden;
  }
  .notebook-spiral {
    position: absolute; left: 10px; top: 14px; bottom: 14px; width: 18px;
    background: repeating-linear-gradient(to bottom, #9aa0ad 0 4px, transparent 4px 14px);
    border-radius: 2px;
  }
  .notebook .brand { font-size: 22px; }
  .notebook-rule { margin-top: 8px; height: 1px; background: rgba(255,255,255,0.55); width: 205px; }
  .notebook-graphic {
    position: absolute; left: 80px; top: 130px; width: 170px; height: 200px;
    background: var(--tint-light);
    border-radius: 50% 50% 40% 40%;
  }

  /* Letterhead */
  .letterhead {
    position: absolute;
    left: 370px; top: 30px;
    width: 420px; height: 543px;
    background: var(--paper);
    box-shadow: var(--shadow);
    padding: 40px 38px;
    overflow: hidden;
  }
  .letterhead .brand { font-size: 22px; }
  .letterhead-rule { margin-top: 8px; height: 1px; background: var(--blue); width: 200px; }
  .letterhead .brand-graphic { top: 250px; right: 0; width: 90px; height: 80px; }
  .letterhead-offices {
    position: absolute; left: 38px; right: 38px; bottom: 34px;
    display: grid; grid-template-columns: 1fr 1fr; gap: 16px;
    border-top: 1px solid #d7dbe6; padding-top: 14px;
  }
  .office-name { font-size: 7.5px; font-weight: 700; letter-spacing: 0.03em; color: var(--blue); text-transform: uppercase; display: flex; align-items: center; gap: 6px; white-space: nowrap; }
  .office-check { width: 9px; height: 9px; border: 1px solid var(--blue); flex: none; }
  .office-lines { margin-top: 5px; font-size: 8px; line-height: 1.6; color: var(--ink-soft); display: grid; grid-template-columns: auto auto; column-gap: 14px; justify-content: start; }

  /* Envelope */
  .envelope {
    position: absolute;
    left: 560px; top: 610px;
    width: 600px; height: 230px;
    background: var(--paper);
    box-shadow: var(--shadow);
    padding: 96px 30px 0;
    overflow: hidden;
  }
  .envelope .brand { font-size: 21px; }
  .envelope-rule { margin-top: 8px; height: 1px; background: var(--blue); width: 190px; }
  .envelope .brand-graphic { top: 0; right: 0; width: 210px; height: 150px; }
  .envelope-return { position: absolute; left: 300px; bottom: 30px; font-size: 8px; color: var(--ink-soft); letter-spacing: 0.04em; text-transform: uppercase; }
</style>
</head>
<body>

  <section class="card card--front" aria-label="Business card front">
    <span class="brand-graphic" role="img" aria-label="Corner brand graphic area"></span>
    <div class="brand"><span class="brand-dot"></span>Ridgeway &amp; Alder</div>
    <p class="card-person">Dr. Lena Marsh</p>
    <p class="card-role">Dentist</p>
    <p class="card-contact">2150 Cedar St., Ridgeway, ON<br><b>T</b> 555-210-4400 &nbsp; <b>F</b> 555-210-4401</p>
  </section>

  <section class="card card--back" aria-label="Business card back">
    <div class="brand brand--light"><span class="brand-dot"></span>Ridgeway &amp; Alder</div>
  </section>

  <section class="notebook" aria-label="Notebook cover">
    <span class="notebook-spiral"></span>
    <div class="brand brand--light"><span class="brand-dot"></span>Ridgeway &amp; Alder</div>
    <div class="notebook-rule"></div>
    <span class="notebook-graphic" role="img" aria-label="Faint brand graphic area"></span>
  </section>

  <section class="letterhead" aria-label="Letterhead">
    <div class="brand"><span class="brand-dot"></span>Ridgeway &amp; Alder</div>
    <div class="letterhead-rule"></div>
    <span class="brand-graphic" role="img" aria-label="Edge brand graphic area"></span>
    <footer class="letterhead-offices">
      <div class="office">
        <p class="office-name"><span class="office-check"></span>Ridgeway Family Dental Centre</p>
        <div class="office-lines">
          <span>T 555-210-4400</span><span>2150 Cedar St.</span>
          <span>F 555-210-4401</span><span>Ridgeway, ON</span>
        </div>
      </div>
      <div class="office">
        <p class="office-name"><span class="office-check"></span>Alder Family Dental Centre</p>
        <div class="office-lines">
          <span>T 555-318-7700</span><span>48 Birch Line Rd.</span>
          <span>F 555-318-7701</span><span>Alder, ON</span>
        </div>
      </div>
    </footer>
  </section>

  <section class="envelope" aria-label="Envelope">
    <span class="brand-graphic" role="img" aria-label="Corner brand graphic area"></span>
    <div class="brand"><span class="brand-dot"></span>Ridgeway &amp; Alder</div>
    <div class="envelope-rule"></div>
    <p class="envelope-return">2150 Cedar St., Ridgeway, ON</p>
  </section>

</body>
</html>
```